Label for a new skin care product

Hello, we are launching a new skin care product. It's a face serum. One product only. I have attached the size requirements and a very general look at what is required. The final result will be a label sticker than gets placed on the bottle.

I have created some (amateur) designs using Canva here: https://www.drafvelo.net/board/QX7tLpWmr2K/hJbnTqzVuRk_-YsDw_4_n/view?utm_content=QX7tLpWmr2K&utm_campaign=boardshare&utm_medium=link2&utm_source=sharebutton

The text is what is required on the label. The design we are seeking is a very simply Wordmark logo with interesting font only. You can see I'm seeking ideas on a colorful design as well as something more ordinary/clinical. The people who will buy this product will be more upper class, well paid, and critical thinkers. Upscale. We don't want too many colors due to printing costs.

Target Market(s)

Female 25-45 years old who are hip and savvy

Requirements
Must have
• wordmark logo

```html
<!DOCTYPE html>
<html lang="en">
<head>
<meta charset="utf-8">
<title>Vela Snail Mucin 96% – Bottle Label</title>
<link rel="stylesheet" href="https://fonts.googleapis.com/css2?family=Didact+Gothic&family=Lato:wght@700&family=Noto+Sans+KR:wght@400;500&family=Questrial&display=swap">
<style>
  :root {
    --page: #fdf3f5;
    --label-top: #ffffff;
    --label-bottom: #f9dbe2;
    --petal: #f3c6d0;
    --petal-deep: #eaa9b8;
    --ink: #111111;
    --text: #2b2b2b;
    --accent: #e0767c;
  }
  * { margin: 0; padding: 0; box-sizing: border-box; }
  html, body { width: 1015px; height: 1200px; overflow: hidden; }
  body {
    background: var(--page);
    font-family: "Didact Gothic", sans-serif;
    color: var(--text);
    position: relative;
  }
  .label {
    position: absolute;
    left: 20px; top: 281px;
    width: 975px; height: 638px;
    background: linear-gradient(180deg, var(--label-top) 0%, #fdf0f3 55%, var(--label-bottom) 100%);
    box-shadow: 0 6px 18px rgba(180, 120, 135, 0.18);
    overflow: hidden;
  }
  .petals {
    position: absolute; inset: 0;
    background:
      radial-gradient(ellipse 130px 170px at 480px 150px, rgba(234,169,184,0.55), transparent 70%),
      radial-gradient(ellipse 110px 90px at 360px 90px, rgba(243,198,208,0.55), transparent 70%),
      radial-gradient(ellipse 120px 110px at 95px 370px, rgba(243,198,208,0.5), transparent 70%),
      radial-gradient(ellipse 90px 60px at 800px 20px, rgba(243,198,208,0.45), transparent 70%);
  }
  .block { position: absolute; text-align: center; }
  .col-left  { left: 48px;  width: 200px; }
  .col-mid   { left: 367px; width: 240px; }
  .col-right { left: 695px; width: 240px; }

  .heading {
    font-family: "Lato", sans-serif; font-weight: 700;
    font-size: 13.5px; letter-spacing: 0.2px; color: var(--text);
  }
  .copy { font-size: 14px; line-height: 17px; }
  .copy b { font-family: "Lato", sans-serif; font-weight: 700; }

  .divider { position: absolute; height: 10px; }
  .divider::before {
    content: ""; position: absolute; left: 0; right: 0; top: 4.5px;
    height: 1px; background: var(--accent);
  }
  .divider::after {
    content: ""; position: absolute; left: 50%; top: 2px;
    width: 6px; height: 6px; margin-left: -3px;
    background: var(--accent); transform: rotate(45deg);
  }

  .wordmark {
    font-family: "Didact Gothic", sans-serif; font-size: 42px;
    color: var(--ink); letter-spacing: 1px; line-height: 1;
  }
  .title {
    font-family: "Questrial", sans-serif; color: var(--ink);
    font-size: 68px; line-height: 57px; letter-spacing: -1px;
  }
  .percent {
    font-family: "Questrial", sans-serif; color: var(--ink);
    font-size: 64px; line-height: 1;
  }
  .subtitle {
    font-size: 20.5px; line-height: 25px; color: var(--accent); letter-spacing: 0.3px;
  }
  .korean { font-family: "Noto Sans KR", sans-serif; }
  .icons { position: absolute; left: 72px; top: 495px; width: 230px; height: 62px; }
</style>
</head>
<body>
  <section class="label" aria-label="Snail Mucin 96% bottle label">
    <div class="petals" role="img" aria-label="Soft pink flower petals drifting across the label"></div>

    <!-- Left column -->
    <h2 class="block col-left heading" style="top:67px;left:38px">SNAIL MUCIN ESSENCE</h2>
    <p class="block col-left copy" style="top:106px;left:40px;width:218px">
      <b>Directions:</b> For a pretty, natural glow apply AM and PM to freshly cleansed face, before all other actives.
    </p>
    <div class="divider" style="top:216px;left:53px;width:190px"></div>
    <p class="block col-left copy" style="top:246px;left:53px;width:190px">
      <b>Caution:</b>&nbsp; External use only. Do not get into your eyes
    </p>
    <svg class="icons" viewBox="0 0 230 62" aria-hidden="true">
      <g fill="var(--ink)">
        <path d="M10 14 Q28 2 44 6 L44 10 Q28 7 10 18 Z"/>
        <rect x="7" y="22" width="37" height="22" rx="3"/>
        <rect x="7" y="18" width="37" height="3"/>
      </g>
      <text x="25.5" y="39" font-family="Lato, sans-serif" font-weight="700" font-size="10" fill="#fff" text-anchor="middle">12M</text>
      <g fill="none" stroke="var(--ink)" stroke-width="4" stroke-linejoin="round">
        <path d="M80 30 L90 14 L100 30"/>
        <path d="M86 36 H100"/>
      </g>
      <g fill="var(--ink)">
        <path d="M76 32 L84 30 L80 38 Z"/>
        <path d="M102 26 L104 34 L96 32 Z"/>
      </g>
      <text x="92" y="56" font-family="Lato, sans-serif" font-weight="700" font-size="10" fill="var(--ink)" text-anchor="middle">PET</text>
      <path d="M148 42 Q146 18 176 14 Q176 38 154 42 L150 46 Z" fill="var(--ink)"/>
    </svg>
    <p class="block col-left copy" style="top:586px;left:64px;width:200px;font-size:12.5px">100 mL / 3.38 fl.oz</p>

    <!-- Centre column -->
    <div class="block col-mid wordmark" style="top:50px">vela</div>
    <h1 class="block col-mid title" style="top:193px;left:337px;width:300px">SNAIL<br>MUCIN</h1>
    <div class="block col-mid percent" style="top:320px">96%</div>
    <div class="divider" style="top:389px;left:393px;width:189px"></div>
    <p class="block col-mid subtitle" style="top:410px;left:347px;width:280px">POWER ESSENCE<br>WITH GOTU KOLA</p>
    <div class="divider" style="top:469px;left:392px;width:189px"></div>
    <p class="block col-mid copy" style="top:497px;left:357px;width:260px;font-size:13px">Paraben,Alcohol,Fragrance, Phthalate,and Cruelty Free</p>
    <p class="block col-mid korean" style="top:573px;font-size:18px">뛰어난 수분 공급</p>

    <!-- Right column -->
    <h2 class="block col-right heading" style="top:67px">KEY INGREDIENTS</h2>
    <p class="block col-right copy" style="top:95px">
      <b>Snail Mucin 96%</b><br>Secretion Filtrate &amp;<br>Gotu Kola
    </p>
    <div class="divider" style="top:169px;left:723px;width:189px"></div>
    <p class="block col-right copy" style="top:205px;left:690px;width:250px">
      Anti-aging Snail Mucin Essence penetrates deeply, provides critical, all day hydration, repairs damage, rebalances and prepares the skin for deeper absorption of serums and moisturizers
    </p>
    <p class="block col-right copy korean" style="top:346px;font-size:12.5px">피부 보습, 다크 스팟 복구, 손상<br>된 피부 재생</p>
    <div class="divider" style="top:402px;left:720px;width:189px"></div>
    <p class="block col-right copy" style="top:423px;left:680px;width:270px">
      <b>Benefits:</b><br>Anti-aging,Collagen Boosting, Healing,Renewal, Scar Treatment, Elasticity, Tone
    </p>
    <p class="block col-right copy" style="top:557px;font-size:13px">www.velaskin.com</p>
    <p class="block col-right copy" style="top:583px;font-family:'Lato',sans-serif;font-weight:700;font-size:13px">Korean-inspired excellence</p>
  </section>
</body>
</html>
```